依頼概要
日常のしぐさをちょっと変えるだけで、自分がなりたい自分に(元気な心になりたい。普段より美しく、カッコよくなりたい等々)なれることを、日本舞踊のしぐさを使って楽しく書きました。
伝統芸能というと堅苦しく、敷居が高いイメージがありますが、実は流行した江戸時代や室町時代では、アイドル的なポップな風俗でもあったのですね。それが型になると固定化してしまいますが、その冷凍保存された精神をまずは溶かして現代でも使えるアイテムにしたいという内容の本です。
そんなわけで、表紙デザインはあくまでもデザイナーさんのイメージにお任せしたいと考えています。ステキに遊んでいただけたら嬉しいです。
表紙には小さくてもいいので、私の着物姿の上半身写真を入れるようにと、森川沙織さんからご指示があったこと付記しておきます。よろしゅうに…堀誠司
たくさんのデザインプランをいただきありがとうございます。
著者が日本舞踊家のこともあり、和テイストのものを多くいただきました。
が、内容も含めて、現代に通じるものにしたいため、和テイストを避けたいと考えて
おります。よろしくお願いいたします。3日間だけ延長させていただきたく存じます。

今回の採用に関しては、数十人のグループによる投票や意見で、最も人気のあったデザインを選ばせていただきました。一位になったデザインは全体の赤がたいへん効果的で、膝だけのカットが大胆かつ、それをカバーの上部に配したのが意表をついてインパクトがありました。次点の作は拙著の趣旨をよく汲んでくださり、仕種のやさしさが秘められているのを感じました。

たくさんの力作揃いで、選ぶのにたいへん困りました。特に拙著の中身をきちんと読み込んでくださっている作は最後まで候補に残りました。私にとって電子書籍は初めてですが、紙の本は10冊ほどになります。それも含めて、今回、惜しくも選には漏れた方から今後も本やさまざまな依頼をさせていただきたいと真剣に考えております。これに懲りずに末永くお付き合いいただければ幸いです。感謝ーーー

```html
<!DOCTYPE html>
<html lang="ja">
<head>
<meta charset="utf-8">
<title>てつきがわたしを軽やかに彩る</title>
<link rel="stylesheet" href="https://fonts.googleapis.com/css2?family=Noto+Serif+JP:wght@600;700;900&family=Noto+Sans+JP:wght@500&display=swap">
<style>
  :root {
    --paper: #f6f5f8;
    --silk: #e4e1ea;
    --ink-purple: #5b3f83;
    --band-lavender: #d9cfe8;
    --panel-purple: #5d4a86;
    --panel-purple-deep: #4a3870;
    --leaf-green: #7fa35a;
    --petal-white: #fbfbf7;
    --text-white: #ffffff;
    --author-ink: #2f2440;
  }
  * { margin: 0; padding: 0; box-sizing: border-box; }
  html, body { width: 750px; height: 1200px; overflow: hidden; }
  body { background: #ffffff; }
  .cover {
    position: relative;
    width: 750px; height: 1200px;
    overflow: hidden;
    background: linear-gradient(160deg, var(--paper) 0%, var(--silk) 45%, #f2f0f5 70%, var(--silk) 100%);
    font-family: "Noto Serif JP", serif;
  }
  .title-band {
    position: absolute;
    left: 578px; top: 0;
    width: 78px; height: 300px;
    background: linear-gradient(180deg, var(--band-lavender) 0%, rgba(217,207,232,0.6) 85%, rgba(217,207,232,0) 100%);
  }
  .flowers-top {
    position: absolute; left: 0; top: 0; width: 300px; height: 290px;
    background:
      radial-gradient(circle at 40% 35%, var(--petal-white) 0 22%, rgba(251,251,247,0) 40%),
      radial-gradient(circle at 75% 30%, rgba(127,163,90,0.7) 0 15%, rgba(127,163,90,0) 45%),
      radial-gradient(ellipse at 30% 60%, rgba(127,163,90,0.75) 0 30%, rgba(127,163,90,0) 70%);
  }
  .flowers-bottom {
    position: absolute; left: 0; top: 540px; width: 540px; height: 332px;
    background:
      radial-gradient(circle at 20% 55%, var(--petal-white) 0 14%, rgba(251,251,247,0) 26%),
      radial-gradient(circle at 46% 40%, var(--petal-white) 0 11%, rgba(251,251,247,0) 22%),
      radial-gradient(circle at 60% 80%, var(--petal-white) 0 10%, rgba(251,251,247,0) 20%),
      radial-gradient(ellipse at 35% 60%, rgba(110,150,78,0.85) 0 35%, rgba(110,150,78,0) 72%);
  }
  .title-col {
    position: absolute;
    writing-mode: vertical-rl;
    color: var(--ink-purple);
    font-weight: 700;
    line-height: 1;
    white-space: nowrap;
  }
  .title-col .big { font-size: 120px; font-weight: 900; }
  .title-col .small { font-size: 62px; }
  .col-first { left: 560px; top: 40px; }
  .col-first .big { letter-spacing: 6px; }
  .col-second { left: 366px; top: 160px; }
  .col-third { left: 216px; top: 268px; }
  .author {
    position: absolute;
    left: 64px; top: 350px;
    writing-mode: vertical-rl;
    color: var(--author-ink);
    font-weight: 700;
    font-size: 54px;
    line-height: 1;
    letter-spacing: 4px;
  }
  .author .role { font-size: 32px; font-weight: 600; margin-top: 14px; }
  .blurb-panel {
    position: absolute; left: 0; top: 872px;
    width: 750px; height: 328px;
    background: linear-gradient(180deg, var(--panel-purple) 0%, var(--panel-purple-deep) 100%);
  }
  .portrait {
    position: absolute; left: 52px; top: 905px;
    width: 192px; height: 192px; border-radius: 50%;
    background: radial-gradient(circle at 50% 40%, #d8c3ad 0%, #9a8a80 55%, #5b4e55 100%);
    border: 4px solid rgba(255,255,255,0.85);
  }
  .blurb {
    position: absolute; left: 296px; top: 925px;
    color: var(--text-white);
    font-family: "Noto Sans JP", sans-serif;
    font-weight: 500;
    font-size: 29px;
    line-height: 61px;
    white-space: nowrap;
  }
</style>
</head>
<body>
  <main class="cover">
    <div class="flowers-top" role="img" aria-label="白い花と緑の葉の写真"></div>
    <div class="flowers-bottom" role="img" aria-label="白い花と緑の葉の写真"></div>
    <div class="title-band"></div>

    <h1 class="title">
      <span class="title-col col-first"><span class="big">てつき</span><span class="small">がわたしを</span></span>
      <span class="title-col col-second"><span class="big">軽</span><span class="small">やかに</span></span>
      <span class="title-col col-third"><span class="big">彩</span><span class="small">る</span></span>
    </h1>

    <p class="author">堀誠司<span class="role">著</span></p>

    <section class="blurb-panel"></section>
    <div class="portrait" role="img" aria-label="着物姿の著者の上半身写真"></div>
    <p class="blurb">
      日常の何気ない「しぐさ」に<br>
      日本舞踊をはじめとした<br>
      伝統芸能の所作をとりいれて<br>
      「自分がなりたい自分」になる!
    </p>
  </main>
</body>
</html>
```